U.S. Popcorn company needs business cards

We are a popcorn company that manufactures popcorn and sells it to grocery stores worldwide. Our theme is "Americana" and our logo is U.S. route 66 which is the most famous highway in the U.S.

We would like the design to be simple and to use both sides. On the back side we would like to see just the logo and website. The front would be normal details

Target Market(s)

Wholesalers, grocers and distributors

Industry/Entity Type

Manufacture

Contact Information for Business Card

Business name: Bluebell Ridge Popcorn
Phone: +1 555 014 2286
Email: Derek@bluebellridgepopcorn.com
website: www.bluebellridgepopcorn.com
Tag Line: "FRESHLY POPPED DAILY"
Name: Derek Halvorsen
Title: Founder/President

Requirements
Must have
• Either this design should be fun or clean and simple. I will let you show me your thougths.
Nice to have
• Anything that ties in the real Hwy Route 66.
• Colors might need to be red, white and blue incorporated.
Should not have
• Not be too busy.

```html
<!DOCTYPE html>
<html lang="en">
<head>
<meta charset="utf-8">
<title>Bluebell Ridge Popcorn – Business Cards</title>
<link rel="stylesheet" href="https://fonts.googleapis.com/css2?family=Roboto:wght@400;500&family=Andika:wght@400;700&display=swap">
<style>
  :root {
    --navy: #233066;
    --red: #ec2227;
    --white: #ffffff;
    --page: #ecebe8;
    --road-light: #f6f6f6;
    --road-mid: #e2e3e4;
    --road-dark: #d3d4d5;
  }
  * { box-sizing: border-box; margin: 0; padding: 0; }
  html, body { width: 900px; height: 1200px; overflow: hidden; }
  body {
    position: relative;
    background: var(--page);
    font-family: "Roboto", Arial, sans-serif;
  }
  .card {
    position: absolute;
    left: 90px;
    width: 715px;
    border-radius: 26px;
    overflow: hidden;
    box-shadow: 0 6px 16px rgba(0,0,0,0.18);
  }
  .card-front { top: 145px; height: 412px; background: var(--white); }
  .card-back { top: 640px; height: 413px; background: var(--red); }

  .road-photo {
    position: absolute; inset: 0;
    background: linear-gradient(180deg, var(--road-light) 0%, var(--road-light) 45%, var(--road-mid) 70%, var(--road-dark) 100%);
  }
  .brand-name {
    position: absolute;
    display: flex; align-items: center; justify-content: center;
    text-align: center;
    font-family: "Roboto", Arial, sans-serif;
    font-weight: 500;
    line-height: 1.15;
  }
  .card-front .brand-name {
    left: 85px; top: 95px; width: 230px; height: 215px;
    color: var(--navy); font-size: 32px;
  }
  .divider {
    position: absolute; left: 357px; top: 152px;
    width: 2px; height: 106px; background: var(--navy);
  }
  .contact { position: absolute; left: 399px; top: 146px; color: var(--navy); }
  .contact-name { font-size: 25px; font-weight: 500; line-height: 1; }
  .contact-title { color: var(--red); font-size: 14px; margin-top: 6px; }
  .contact-list { list-style: none; margin-top: 10px; font-size: 15px; font-weight: 500; }
  .contact-list li { display: flex; align-items: center; height: 22px; }
  .contact-list svg { width: 16px; height: 14px; margin-right: 7px; flex: none; }
  .icon-fill { fill: var(--red); }
  .icon-line { fill: none; stroke: var(--red); stroke-width: 1.4; }
  .tagline {
    position: absolute; left: 51px; right: 47px; top: 353px;
    display: flex; align-items: center; gap: 14px;
    font-family: "Andika", Arial, sans-serif; font-size: 20px; letter-spacing: 0.5px;
    white-space: nowrap;
  }
  .tagline::before, .tagline::after { content: ""; flex: 1; height: 2px; background: var(--navy); }
  .tagline-navy { color: var(--navy); }
  .tagline-red { color: var(--red); }

  .card-back .brand-name {
    left: 215px; top: 60px; width: 285px; height: 265px;
    color: var(--white); font-size: 40px;
  }
  .back-web {
    position: absolute; left: 0; right: 0; top: 354px;
    text-align: center; color: var(--white);
    font-family: "Andika", Arial, sans-serif; font-weight: 700; font-size: 20px;
  }
</style>
</head>
<body>
  <section class="card card-front">
    <div class="road-photo" role="img" aria-label="Faded photograph of an open desert highway with a painted route shield on the asphalt"></div>
    <div class="brand-name">Bluebell Ridge Popcorn</div>
    <div class="divider"></div>
    <div class="contact">
      <p class="contact-name">Derek Halvorsen</p>
      <p class="contact-title">Founder/President</p>
      <ul class="contact-list">
        <li><svg viewBox="0 0 16 14"><path class="icon-fill" d="M1 5c0-2 3-4 7-4s7 2 7 4v1h-3V4.5H4V6H1zM3 7h10l2 6H1z"/></svg>+1 555 014 2286</li>
        <li><svg viewBox="0 0 16 14"><rect class="icon-line" x="1.5" y="2.5" width="13" height="9"/><path class="icon-line" d="M1.5 2.5 8 8l6.5-5.5"/></svg>Derek@bluebellridgepopcorn.com</li>
        <li><svg viewBox="0 0 16 14"><circle class="icon-line" cx="8" cy="7" r="6"/><ellipse class="icon-line" cx="8" cy="7" rx="2.6" ry="6"/><path class="icon-line" d="M2 7h12"/></svg>www.bluebellridgepopcorn.com</li>
      </ul>
    </div>
    <p class="tagline"><span><span class="tagline-navy">FRESHLY</span> <span class="tagline-red">POPPED DAILY</span></span></p>
  </section>

  <section class="card card-back">
    <div class="brand-name">Bluebell Ridge Popcorn</div>
    <p class="back-web">www.bluebellridgepopcorn.com</p>
  </section>
</body>
</html>
```